LTV Brochure Design Project

We need a 4 page brochure (A4 size) prepared to announce a new consulting service. The consulting service is highly professional and is aimed at business owners of small to medium businesses and their accountants.

Thankyou for the designs posted so far, please see a new file uploaded that has hi-res diagrams for the brochure, regards

please use the hi res graphics I uploaded today, thanks

Thankyou for your designs please: 1) put the title on the front page ie "A unique Offering to Business Owners" should be on the first page 2) please upload all 4 pages so that I can see that the text fits well across 4 pages 3) please use the hi res graphics in the file uploaded yesterday.

Thanks again!

Designers - please note the original brief: it must fit on a brochure 4 x A4 pages (ie A3 folded brochure)

business owners of companies worth $3M to $30M + accountants, lawyers and other professionals

Business

• Must appear professional - not gimicky

```html
<!DOCTYPE html>
<html lang="en">
<head>
<meta charset="utf-8">
<title>LTV Brochure – A Unique Offering to Business Owners</title>
<link href="https://fonts.googleapis.com/css2?family=Cinzel:wght@500;600&family=Arimo:ital,wght@0,400;0,700;1,400;1,700&display=swap" rel="stylesheet">
<style>
:root{
  --stage:#8d8f93;
  --paper:#f2f3f5;
  --ink:#4a4b50;
  --dark:#221f22;
  --gold:#f5e000;
  --title-gold:#e9d36a;
  --navy:#2c3a6b;
  --lead-blue:#2a3a8c;
  --blue:#1c8fd6;
  --blue-deep:#0d5f9e;
  --accent-red:#c4161c;
  --green:#5a9a3a;
  --num-green:#1f9d57;
  --c-fin:#213a6b;
  --c-sus:#7a1e22;
  --c-comp:#6a7d1e;
  --c-cust:#5b2c6a;
  --c-exp:#c0561d;
}
*{box-sizing:border-box;margin:0;padding:0}
html,body{width:877px;height:1200px;overflow:hidden}
body{background:var(--stage);font-family:"Arimo",Arial,sans-serif;color:var(--ink);position:relative}
.page{position:absolute;width:396px;height:558px;background:var(--paper);overflow:hidden;box-shadow:0 2px 6px rgba(0,0,0,.45)}
.p-inner-left{left:28px;top:28px}
.p-cover{left:453px;top:28px;background:var(--dark)}
.p-why{left:28px;top:614px}
.p-benefits{left:453px;top:614px}

.masthead{position:absolute;left:0;top:0;width:396px;height:58px;background:var(--dark)}
.masthead::after{content:"";position:absolute;left:0;right:0;bottom:0;height:4px;background:linear-gradient(90deg,#cfd2d8,#fff 50%,#cfd2d8)}
.masthead-title{position:absolute;left:24px;top:26px;font-family:"Cinzel",serif;font-weight:500;font-size:10.4px;color:var(--title-gold);letter-spacing:.3px}
.brand-box{position:absolute;left:278px;top:20px;width:96px;height:56px;border:2px solid #111;background:#2a2b30;display:flex;align-items:flex-end;justify-content:flex-end;padding:0 6px 6px 0;z-index:2}
.brand-name{font-size:6px;color:var(--gold);display:flex;align-items:center;gap:3px}
.brand-name i{display:inline-block;width:5px;height:5px;border-radius:50%;background:var(--gold)}

.footer{position:absolute;left:0;bottom:0;width:396px;height:24px;background:var(--dark)}
.footer-band{position:absolute;left:0;top:0;width:100%;height:18px;background:var(--gold);display:flex;align-items:center;justify-content:space-around;font-size:8px;color:#222}
.footer-band .dot{width:5px;height:5px;border-radius:50%;border:1.5px solid #555}

.body{position:absolute;font-size:5.6px;line-height:7.2px;color:var(--ink)}
.body p{margin-bottom:5px}
.lead{font-style:italic;color:var(--lead-blue);font-size:6.4px;line-height:8.4px}
.lead.bold{font-weight:700;color:#444;font-size:6.6px;line-height:8.6px}

.dot-list{list-style:none}
.dot-list li{position:relative;padding-left:9px;margin-bottom:7px}
.dot-list li::before{content:"";position:absolute;left:0;top:1.5px;width:4px;height:4px;border-radius:50%;background:var(--green);box-shadow:0 0 0 1px #cde3c1}
.dot-list b{color:var(--accent-red)}
.tick-list{list-style:none}
.tick-list li{position:relative;padding-left:12px;margin-bottom:7px}
.tick-list li::before{content:"";position:absolute;left:1px;top:1px;width:5px;height:5px;border:1px solid var(--navy)}
.tick-list li::after{content:"";position:absolute;left:2.5px;top:0;width:3px;height:5px;border:solid var(--navy);border-width:0 1.3px 1.3px 0;transform:rotate(40deg)}
.red-list{list-style:none;padding-left:6px}
.red-list li{position:relative;padding-left:8px;margin-bottom:3.4px}
.red-list li::before{content:"";position:absolute;left:0;top:1.5px;width:4px;height:4px;border-radius:50%;background:var(--accent-red)}

.section-pill{position:absolute;left:28px;width:340px;height:19px;border-radius:9.5px;background:linear-gradient(180deg,#3fb2ee,var(--blue) 55%,var(--blue-deep));display:flex;align-items:center;padding-left:29px;font-weight:700;font-size:10.4px;color:var(--gold)}
.section-pill::before{content:"";position:absolute;left:-4px;top:1px;width:27px;height:17px;border-radius:50%;background:radial-gradient(circle at 50% 40%,#666,#1a1a1a 70%);border:1px solid #111}

.pillars{position:absolute;left:24px;top:344px;width:350px;height:180px}
.pillars-title{font-size:8px;color:#333}
.pillar-brand{position:absolute;right:2px;top:-2px;font-size:8px;color:#555;display:flex;align-items:center;gap:3px}
.pillar-brand i{display:inline-block;width:6px;height:6px;background:#555}
.pillar{position:absolute;top:18px;width:52px}
.pillar-head{height:25px;color:#fff;font-size:5.2px;display:flex;align-items:center;justify-content:center;text-align:center;border:1px solid rgba(0,0,0,.4);line-height:1.2}
.pillar-item{position:absolute;left:9px;width:42px;height:25px;font-size:4.6px;text-align:center;display:flex;align-items:center;justify-content:center;line-height:1.15;border:1px solid;border-radius:1px}
.pillar-line{position:absolute;left:3px;top:25px;width:1px;height:116px;background:#888}
.pillar-item::before{content:"";position:absolute;left:-7px;top:50%;width:6px;height:1px;background:#888}
.copyright{position:absolute;left:2px;bottom:0;font-size:4.4px;color:#444}

.cover-photo{position:absolute;left:0;top:0}
.cover-logo{position:absolute;left:120px;top:388px;width:157px;height:84px;border:3px solid #0a0a0a;background:#2a2b30;display:flex;align-items:flex-end;justify-content:flex-end;padding:0 10px 9px 0}
.cover-logo .brand-name{font-size:8px}
.cover-logo .brand-name i{width:6px;height:6px}
.cover-title{position:absolute;left:0;right:0;top:500px;text-align:center;font-family:"Cinzel",serif;font-weight:500;font-size:15px;color:#fff;letter-spacing:.4px}
.cover-strip{position:absolute;left:0;right:0;bottom:0;height:9px;background:var(--gold)}

.numbered{position:absolute;font-size:5.6px;line-height:7.2px}
.num{position:absolute;left:0;top:-4px;font-size:16px;line-height:16px;color:var(--num-green)}
.num-text{padding-left:13px}
</style>
</head>
<body>

<section class="page p-inner-left">
  <header class="masthead">
    <h2 class="masthead-title">A Unique Offering to Business Owners</h2>
    <div class="brand-box"><span class="brand-name"><i></i>Meridel Advisory</span></div>
  </header>

  <div class="body" style="top:88px;left:37px;right:32px">
    <ul class="dot-list">
      <li><b>Presentation of outcomes:</b> the consultant will then meet with the client to present the outcomes of the Divestment Readiness Assessment. The consultant will provide the client with the complete Divestment Readiness Report at that meeting and will schedule a follow-up meeting. The presentation will typically take 2 hours.</li>
      <li><b>Follow-up:</b> typically within 2 -4 weeks of presenting the Divestment Readiness Report, the consultant will meet with the client to answer any specific questions and to discuss next steps (if applicable).</li>
      <li><b>Optional session with the M&amp;A Specialist:</b> should the client wish to learn more of the M&amp;A process, the consultant will facilitate a session with the M&amp;A Specialist to provide an overview of the sales process and to respond to any questions the client may have.</li>
      <li><b>Optional implementation support:</b> should the client have an interest in gaining assistance to implement some or all of the recommendations, the consultant will develop a proposal tailored to the client's needs.</li>
    </ul>
  </div>

  <h3 class="section-pill" style="top:188px">HIGH QUALITY PROCESS</h3>

  <div class="body" style="top:210px;left:30px;right:30px">
    <p class="lead" style="margin-bottom:4px">The Divestment Readiness Assessment draws on over 26 years of business sale expertise</p>
    <p>The Divestment Readiness Assessment is designed to provide a client with highly qualified, independent advice that is in the best interests of the client:</p>
    <ul class="tick-list">
      <li>The Divestment Readiness Assessment is conducted by an experienced professional that is well informed in the M&amp;A process for small to medium businesses</li>
      <li>The consultant's analysis is reviewed and endorsed by the M&amp;A Specialist</li>
      <li>The Divestment Readiness Assessment is based on the established "5 Pillars" framework which considers the key assessment criteria of buyers that are common across various industries</li>
      <li>Preservation of the client's confidentiality during the process is of paramount importance to the consultant. The Divestment Readiness Assessment includes appropriate measures to support the client's confidentiality. For example, the consultant will allocate a unique reference identifier to the client so the identity of the client is not revealed to the M&amp;A Specialist, nor is it disclosed on any documentation developed by the consultant.</li>
    </ul>
  </div>

  <div class="pillars">
    <div class="pillars-title">Halvern Corp: "5 Pillars" of Sellability</div>
    <div class="pillar-brand"><i></i>HALVERN CORP</div>

    <div class="pillar" style="left:19px">
      <div class="pillar-head" style="background:var(--c-fin)">Financial</div>
      <div class="pillar-line"></div>
      <div class="pillar-item" style="top:32px;background:#e4ebf6;border-color:#6b86b8">Profitability Trend</div>
      <div class="pillar-item" style="top:63px;background:#e4ebf6;border-color:#6b86b8">Cash Flow &amp; Working Capital</div>
      <div class="pillar-item" style="top:96px;background:#e4ebf6;border-color:#6b86b8">Company Size</div>
      <div class="pillar-item" style="top:128px;background:#e4ebf6;border-color:#6b86b8">Valuation/ROI</div>
    </div>
    <div class="pillar" style="left:84px">
      <div class="pillar-head" style="background:var(--c-sus)">Sustainability</div>
      <div class="pillar-line"></div>
      <div class="pillar-item" style="top:32px;background:#f6e3e3;border-color:#b96a6a">Governance &amp; Risk Management</div>
      <div class="pillar-item" style="top:63px;background:#f6e3e3;border-color:#b96a6a">Management Team &amp; Independence from Owners</div>
      <div class="pillar-item" style="top:96px;background:#f6e3e3;border-color:#b96a6a">Systems &amp; Processes</div>
      <div class="pillar-item" style="top:128px;background:#f6e3e3;border-color:#b96a6a">Flexibility across Supply Chain</div>
    </div>
    <div class="pillar" style="left:149px">
      <div class="pillar-head" style="background:var(--c-comp)">Competitive Positioning</div>
      <div class="pillar-line"></div>
      <div class="pillar-item" style="top:32px;background:#eef2dc;border-color:#99a860">Differentiating Offering</div>
      <div class="pillar-item" style="top:63px;background:#eef2dc;border-color:#99a860">Barriers to Entry</div>
      <div class="pillar-item" style="top:96px;background:#eef2dc;border-color:#99a860">Contracts with Customers, Suppliers &amp; Stakeholders</div>
      <div class="pillar-item" style="top:128px;background:#eef2dc;border-color:#99a860">Staff Skills &amp; Retention Risk</div>
    </div>
    <div class="pillar" style="left:213px">
      <div class="pillar-head" style="background:var(--c-cust)">Customer &amp; Industry Dynamics</div>
      <div class="pillar-line"></div>
      <div class="pillar-item" style="top:32px;background:#ece3f0;border-color:#8f6b9e">Recurring Revenue</div>
      <div class="pillar-item" style="top:63px;background:#ece3f0;border-color:#8f6b9e">Client Concentration</div>
      <div class="pillar-item" style="top:96px;background:#ece3f0;border-color:#8f6b9e">Industry &amp; Government Regulations</div>
      <div class="pillar-item" style="top:128px;background:#ece3f0;border-color:#8f6b9e">External Funding Dynamics</div>
    </div>
    <div class="pillar" style="left:278px">
      <div class="pillar-head" style="background:var(--c-exp)">Expansion Opportunities</div>
      <div class="pillar-line"></div>
      <div class="pillar-item" style="top:32px;background:#fbe8dc;border-color:#d98a5a">Scalability</div>
      <div class="pillar-item" style="top:63px;background:#fbe8dc;border-color:#d98a5a">Tangible Opportunities for Growth</div>
      <div class="pillar-item" style="top:96px;background:#fbe8dc;border-color:#d98a5a">Industry Growth rate</div>
      <div class="pillar-item" style="top:128px;background:#fbe8dc;border-color:#d98a5a">Market Share</div>
    </div>
    <div class="copyright">©2013. Halvern Capital Pty Ltd. Commercial in Confidence</div>
  </div>

  <footer class="footer"><div class="footer-band"><span>info@MeridelAdvisory.com</span><span class="dot"></span><span>000-555-0142</span><span class="dot"></span><span>www.MeridelAdvisory.com</span></div></footer>
</section>

<section class="page p-cover">
  <svg class="cover-photo" width="396" height="310" viewBox="0 0 396 310">
    <defs>
      <radialGradient id="tunnel" cx="50%" cy="45%" r="60%">
        <stop offset="0" stop-color="#0b1f4a"/>
        <stop offset=".45" stop-color="#2f6fc4"/>
        <stop offset="1" stop-color="#0a1c44"/>
      </radialGradient>
    </defs>
    <path role="img" aria-label="Abstract blue light tunnel photograph" d="M0 0 H396 V180 Q340 300 198 300 Q56 300 0 180 Z" fill="url(#tunnel)"/>
  </svg>
  <div class="cover-logo"><span class="brand-name"><i></i>Meridel Advisory</span></div>
  <h1 class="cover-title">A Unique Offering to Business Owners</h1>
  <div class="cover-strip"></div>
</section>

<section class="page p-why">
  <header class="masthead">
    <h2 class="masthead-title">A Unique Offering to Business Owners</h2>
    <div class="brand-box"><span class="brand-name"><i></i>Meridel Advisory</span></div>
  </header>

  <h3 class="section-pill" style="top:91px">WHY CONDUCT A DIVESTMENT READINESS ASSESSMENT?</h3>
  <div class="body" style="top:117px;left:28px;right:28px">
    <p class="lead bold" style="margin-bottom:6px">70% of owners of small and medium businesses will seek to exit their business over the next 10 years.</p>
    <p>Approximately 80% of Australian businesses are owned by baby boomers, who tend to have most of their wealth locked in their business. As baby boomers enter their 60s and 70s over the coming decade most will need to exit their businesses to unlock funds for retirement.</p>
    <p>As a result, more than two-thirds of all Australian SMEs will seek to exit within a single decade, flooding the market with businesses for sale – creating what is being referred to as the "Baby Boomer Tsunami".</p>
    <p>With so many businesses for sale on the market, many owners will be unable to exit - or sell for fair value, leaving them with significantly reduced funds for retirement.</p>
    <p>To unlock the maximum value within what is in most cases, their largest asset, owners must ensure their businesses are exceptionally well prepared and ready for sale. Given that 75% of business owners have no exit strategy, Australian private companies will need to act to avert a crisis.</p>
  </div>

  <h3 class="section-pill" style="top:239px">WHAT IS A DIVESTMENT READINESS ASSESSMENT?</h3>
  <div class="body" style="top:266px;left:28px;right:28px">
    <p class="lead bold">The Divestment Readiness Assessment (LTV) provides an independent assessment of the readiness of a business for sale and where appropriate, identifies the specific initiatives that would optimise the sale outcome for the business owner.</p>
  </div>
  <div class="body" style="top:300px;left:28px;width:160px">
    <p>The LTV is conducted by consulting professionals and is supported by M&amp;A Specialists. It provides the business owner with the following:</p>
  </div>

  <svg style="position:absolute;left:196px;top:298px" width="172" height="114" viewBox="0 0 172 114" font-family="Arimo,sans-serif">
    <rect x="14" y="2" width="154" height="96" fill="#e3e8f1"/>
    <line x1="91" y1="2" x2="91" y2="98" stroke="#7b8fb8" stroke-width=".6"/>
    <line x1="14" y1="50" x2="168" y2="50" stroke="#7b8fb8" stroke-width=".6"/>
    <line x1="14" y1="98" x2="14" y2="0" stroke="#222" stroke-width=".8"/>
    <line x1="14" y1="98" x2="170" y2="98" stroke="#222" stroke-width=".8"/>
    <path d="M12 3 L14 0 L16 3" fill="none" stroke="#222" stroke-width=".8"/>
    <path d="M167 96 L170 98 L167 100" fill="none" stroke="#222" stroke-width=".8"/>
    <text x="52" y="22" font-size="5.8" font-weight="700" text-anchor="middle" fill="#222">Under</text>
    <text x="52" y="29" font-size="5.8" font-weight="700" text-anchor="middle" fill="#222">Prepared</text>
    <text x="129" y="22" font-size="5.8" font-weight="700" text-anchor="middle" fill="#222">Optimised for</text>
    <text x="129" y="29" font-size="5.8" font-weight="700" text-anchor="middle" fill="#222">Sale</text>
    <text x="52" y="75" font-size="5.8" font-weight="700" text-anchor="middle" fill="#222">Premature</text>
    <text x="129" y="75" font-size="5.8" font-weight="700" text-anchor="middle" fill="#222">Sub Potential</text>
    <text x="8" y="50" font-size="5.2" fill="#2a3a8c" text-anchor="middle" transform="rotate(-90 8 50)">Relative Financial Performance</text>
    <text x="91" y="109" font-size="5.8" fill="#2a3a8c" text-anchor="middle">Relative Ease of Sale</text>
  </svg>

  <div class="numbered" style="top:334px;left:28px;width:160px">
    <span class="num">1</span>
    <div class="num-text">
      <p style="margin-bottom:7px">The overall preparedness of their business for sale in the short-term. This considers 2 dimensions:</p>
      <p style="margin-bottom:7px;padding-left:6px">a. The relative ease with which the business can be sold based on its current structure in the current market.</p>
      <p style="margin-bottom:7px;padding-left:6px">and</p>
      <p style="padding-left:6px">b. The relative financial performance of the business compared with its potential.</p>
    </div>
  </div>
  <div class="numbered" style="top:427px;left:28px;right:28px">
    <span class="num">2</span>
    <p class="num-text">An appraisal that provides the assessed value range of the business in its current state if presented to market in the short-term. The appraisal considers the attractiveness of the business to a variety of buyers such as financial investors and industry acquirers.</p>
  </div>
  <div class="numbered" style="top:463px;left:28px;right:28px">
    <span class="num">3</span>
    <p class="num-text" style="margin-bottom:6px">The high priority initiatives that would make the business more saleable and/or substantially improve the anticipated sale price of the business.</p>
    <p class="num-text">The Divestment Readiness Assessment is focused on identifying those initiatives that will substantially enhance the sale outcome for the owner – as opposed to general business improvement.</p>
  </div>
  <div class="numbered" style="top:513px;left:28px;right:28px">
    <span class="num">4</span>
    <p class="num-text">An example of their business' investment highlights as would be presented to the market if they wish to progress to a sale.</p>
  </div>

  <footer class="footer"><div class="footer-band"><span>info@MeridelAdvisory.com</span><span class="dot"></span><span>000-555-0142</span><span class="dot"></span><span>www.MeridelAdvisory.com</span></div></footer>
</section>

<section class="page p-benefits">
  <header class="masthead">
    <h2 class="masthead-title">A Unique Offering to Business Owners</h2>
    <div class="brand-box"><span class="brand-name"><i></i>Meridel Advisory</span></div>
  </header>

  <div class="body" style="top:82px;left:30px;width:130px">
    <p style="margin-bottom:8px">Additionally, if the client has an interest in understanding more of the process that would be applied to sell their business, the consultant will facilitate a session with an M&amp;A Specialist which will include:</p>
    <ul class="tick-list">
      <li>An overview of the sale process</li>
      <li>Indicative target acquirers for the client's business</li>
      <li>Marketing approach and channels that are applicable to the client's business</li>
      <li>Responses to frequently asked questions such as "how does the M&amp;A Specialist maintain the confidentiality of a business during the sale process?"</li>
    </ul>
  </div>

  <svg style="position:absolute;left:172px;top:90px" width="206" height="130" viewBox="0 0 206 130" font-family="Arimo,sans-serif">
    <line x1="20" y1="0" x2="20" y2="108" stroke="#222" stroke-width=".8"/>
    <line x1="20" y1="108" x2="204" y2="108" stroke="#222" stroke-width=".8"/>
    <path d="M42 108 V70 H94 Q104 30 122 20 Q139 8 176 8" fill="none" stroke="#222" stroke-width=".7"/>
    <line x1="94" y1="70" x2="94" y2="108" stroke="#2a3a8c" stroke-width=".6"/>
    <line x1="122" y1="20" x2="122" y2="108" stroke="#2a3a8c" stroke-width=".6"/>
    <line x1="148" y1="10" x2="148" y2="108" stroke="#2a3a8c" stroke-width=".6"/>
    <line x1="114" y1="28" x2="96" y2="40" stroke="#222" stroke-width=".5"/>
    <rect x="44" y="4" width="64" height="21" fill="#fff" stroke="#ccc" stroke-width=".4"/>
    <text x="76" y="12.5" font-size="6.4" text-anchor="middle" fill="#333">Sale Optimisation</text>
    <text x="76" y="21" font-size="6.4" text-anchor="middle" fill="#333">Recommendations</text>
    <text x="68" y="83" font-size="6.4" text-anchor="middle" fill="#333">Premature</text>
    <text x="135" y="54" font-size="6.4" text-anchor="middle" fill="#333">Optimised</text>
    <text x="135" y="62" font-size="6.4" text-anchor="middle" fill="#333">to sell</text>
    <text x="178" y="28" font-size="6.4" text-anchor="middle" fill="#333">Optimised</text>
    <text x="178" y="36" font-size="6.4" text-anchor="middle" fill="#333">to retain</text>
    <text x="11" y="54" font-size="6.4" fill="#2a3a8c" text-anchor="middle" transform="rotate(-90 11 54)">Anticipated sale outcome</text>
    <text x="108" y="122" font-size="6.8" fill="#2a3a8c" text-anchor="middle">Improvement Effort</text>
  </svg>

  <h3 class="section-pill" style="top:226px">BENEFITS TO THE CLIENT</h3>
  <div class="body" style="top:252px;left:30px;right:30px">
    <p class="lead" style="margin-bottom:6px">The Divestment Readiness Assessment is intended to be an ideal interim phase for any client that wishes to assess and/or optimise their business for sale – whether or not they intend to sell in the short-term.</p>
    <p>The Divestment Readiness Assessment is a consulting engagement designed to provide a client with independent advice regarding their exit options and the readiness of their business for sale. At no stage during the Divestment Readiness Assessment is there an expectation that a client will proceed to a sale.</p>
    <p>The Divestment Readiness Assessment is designed to deliver the following benefits to a client:</p>
    <ul class="red-list">
      <li>Provide independent advice that is in the best interests of the client</li>
      <li>Greatly assist the client to decide whether they should proceed with a sale in the short-term</li>
      <li>Identify specific actions that are expected to substantially improve the client's sale outcome</li>
      <li>Enable the client to understand the likely value they will achieve at exit</li>
      <li>Provide the client with an understanding of the sale process</li>
      <li>Serve as a "stepping-stone" for client who wish to consider selling in the future</li>
      <li>Capture key information that would "kick-start" the client's Information Memorandum and disclosure documentation should the client wish to proceed to sale</li>
    </ul>
  </div>

  <h3 class="section-pill" style="top:405px">DIVESTMENT READINESS ASSESSMENT PROCESS</h3>
  <div class="body" style="top:430px;left:30px;right:30px">
    <p class="lead" style="margin-bottom:5px">Unlike generalist consulting reviews, the Divestment Readiness Assessment is a specialist activity focused on assessing and optimising the potential business sale outcome</p>
    <p>The Divestment Readiness Assessment is conducted as follows:</p>
    <ul class="dot-list" style="padding-left:4px">
      <li><b>Introduction:</b> the consultant provides an overview of the LTV process and outlines key information that is required to support the Review</li>
      <li><b>Onsite review:</b> the consultant will meet the client and tour the client's business if applicable. The consultant will work through the review with the client (typically half a day to a full day)</li>
      <li><b>Analysis:</b> the consultant will work with the M&amp;A Specialist to analyse the information, assess the readiness of the business for sale and to complete the current market value range of the business.</li>
    </ul>
  </div>

  <footer class="footer"><div class="footer-band"><span>info@MeridelAdvisory.com</span><span class="dot"></span><span>000-555-0142</span><span class="dot"></span><span>www.MeridelAdvisory.com</span></div></footer>
</section>

</body>
</html>
```